GOLD COMB label

GOLD COMB – Concept Brief

We are designing a label for our premium honey brand, GOLD COMB. Our goal is to create a bold, prestigious, and proudly African aesthetic that reflects the product's purity, ethical sourcing, and exceptional quality.

Key Design Elements:

1. Brand Name Emphasis:

The word GOLD should be large, bold, eye catching, and prominent, drawing immediate attention.

The word COMB should also be noticeable but doesn’t need to be as dominant as GOLD.

2. Visual Theme:

Incorporate African tapestry patterns, ideally within an outline of the African continent or as part of the background design.

The patterns should evoke a sense of tradition, heritage, and authenticity.

3. Text and Messaging:

A clear statement that the honey is:

Natural, raw, Organic Certified, and Ethically Produced.

Sourced from Zambia's pristine Miombo Forests.

Emphasize that this is pure, unadulterated honey of the highest quality.

4. Aesthetic and Impact:

The design should be elegant and prestigious, reinforcing the message that Africa represents quality.

Use rich, earthy tones with bold highlights to ensure the bottle stands out on the shelf and conveys purity and authenticity. Perhaps some use of gold foil in the label or logo.

5. Overall Feel:

The label should exude a sense of luxury while maintaining a strong African identity.

Balancing boldness with elegance will ensure the product feels premium yet natural.

Logo Text

GOLD COMB followed by some of the ideas above.

```html
<!DOCTYPE html>
<html lang="en">
<head>
<meta charset="utf-8">
<title>GOLD COMB label</title>
<link href="https://fonts.googleapis.com/css2?family=Cinzel:wght@700;900&family=Libre+Baskerville:wght@700&family=Montserrat:wght@600;800&display=swap" rel="stylesheet">
<style>
  :root {
    --bg: #2a1c18;
    --ink: #0d0a08;
    --gold: #e0b064;
    --gold-deep: #b27a38;
    --copper: #8a5528;
    --cream: #fbf4e0;
  }
  html, body {
    margin: 0;
    padding: 0;
    width: 1200px;
    height: 1200px;
    overflow: hidden;
    background: var(--bg);
  }
  .label {
    position: relative;
    width: 1200px;
    height: 1200px;
    background: var(--bg);
  }
  .frame-outer {
    position: absolute;
    left: 113px; top: 63px;
    width: 975px; height: 1059px;
    box-sizing: border-box;
    border: 4px solid var(--gold);
    border-radius: 30px;
    background: var(--ink);
  }
  .frame-inner {
    position: absolute;
    left: 127px; top: 77px;
    width: 947px; height: 1031px;
    box-sizing: border-box;
    border: 2px solid var(--gold-deep);
    border-radius: 22px;
  }
  .tapestry {
    position: absolute;
    left: 133px; top: 83px;
    width: 935px; height: 1019px;
    border-radius: 18px;
    background:
      radial-gradient(ellipse at 50% 50%, rgba(13,10,8,0.55) 0%, rgba(13,10,8,0.15) 60%, rgba(13,10,8,0) 80%),
      linear-gradient(135deg, var(--copper) 0%, var(--gold-deep) 35%, #6e4220 60%, var(--gold-deep) 100%);
  }
  .title-panel {
    position: absolute;
    left: 228px; top: 168px;
    width: 752px; height: 512px;
    background: var(--ink);
    border-radius: 200px 200px 40px 40px / 120px 120px 40px 40px;
  }
  .arc-heading {
    position: absolute;
    left: 380px; top: 168px;
    width: 440px; height: 120px;
  }
  .arc-heading text {
    font-family: "Montserrat", sans-serif;
    font-weight: 800;
    font-size: 40px;
    letter-spacing: 4px;
    fill: var(--cream);
  }
  .sub-heading {
    position: absolute;
    left: 0; top: 222px;
    width: 1200px;
    text-align: center;
    font-family: "Montserrat", sans-serif;
    font-weight: 600;
    font-size: 30px;
    letter-spacing: 4px;
    color: var(--cream);
  }
  .sub-heading .dot { color: var(--gold); margin: 0 10px; }
  .brand-primary, .brand-secondary {
    position: absolute;
    left: 0; width: 1200px;
    text-align: center;
    margin: 0;
    font-family: "Cinzel", serif;
    font-weight: 900;
    color: var(--cream);
    -webkit-text-stroke: 3px var(--gold-deep);
    paint-order: stroke fill;
    line-height: 1;
  }
  .brand-primary {
    top: 255px;
    font-size: 224px;
    letter-spacing: 0;
    transform: scaleY(1.3);
    transform-origin: 50% 0;
  }
  .brand-secondary {
    top: 500px;
    font-size: 198px;
    letter-spacing: 4px;
  }
  .claims-box {
    position: absolute;
    left: 300px; top: 692px;
    width: 618px; height: 316px;
    box-sizing: border-box;
    background: var(--ink);
    border: 3px solid var(--gold-deep);
    border-radius: 22px 22px 60px 60px;
  }
  .claim {
    position: absolute;
    font-family: "Libre Baskerville", serif;
    font-weight: 700;
    color: var(--gold);
    white-space: nowrap;
    line-height: 1;
  }
  .claim-raw { left: 372px; top: 726px; font-size: 36px; }
  .claim-natural { left: 706px; top: 730px; font-size: 32px; }
  .claim-organic { left: 334px; top: 796px; font-size: 34px; }
  .claim-certified { left: 683px; top: 796px; font-size: 34px; }
  .claim-ethical {
    left: 300px; width: 618px; top: 862px;
    text-align: center; font-size: 38px; word-spacing: 12px;
  }
  .origin {
    position: absolute;
    left: 300px; width: 618px; top: 918px;
    margin: 0;
    text-align: center;
    font-family: "Libre Baskerville", serif;
    font-weight: 700;
    font-size: 27px;
    line-height: 36px;
    color: var(--gold-deep);
  }
  .rule {
    position: absolute;
    height: 0;
    border-top: 2px solid var(--gold);
    border-bottom: 2px solid var(--gold-deep);
    padding-top: 2px;
  }
  .rule-left-1 { left: 330px; top: 772px; width: 195px; }
  .rule-right-1 { left: 694px; top: 772px; width: 196px; }
  .rule-left-2 { left: 330px; top: 838px; width: 210px; }
  .rule-right-2 { left: 694px; top: 838px; width: 196px; }
  .continent {
    position: absolute;
    left: 546px; top: 717px;
    width: 120px; height: 134px;
    border-radius: 40% 45% 35% 30%;
    background: linear-gradient(180deg, var(--gold) 0%, var(--gold-deep) 100%);
  }
</style>
</head>
<body>
<main class="label">
  <div class="frame-outer"></div>
  <div class="tapestry" role="img" aria-label="African tapestry pattern border with geometric diamonds, zigzags, flowers and leaves in copper and gold"></div>
  <div class="frame-inner"></div>

  <div class="title-panel"></div>

  <svg class="arc-heading" viewBox="0 0 440 120">
    <defs>
      <path id="premium-arc" d="M 40 112 Q 220 -20 400 112"/>
    </defs>
    <text><textPath href="#premium-arc" startOffset="50%" text-anchor="middle">PREMIUM</textPath></text>
  </svg>
  <div class="sub-heading"><span class="dot">•</span>HONEY<span class="dot">•</span></div>

  <h1 class="brand-primary">GOLD</h1>
  <h2 class="brand-secondary">COMB</h2>

  <section class="claims-box"></section>
  <span class="claim claim-raw">RAW</span>
  <span class="claim claim-natural">NATURAL</span>
  <div class="rule rule-left-1"></div>
  <div class="rule rule-right-1"></div>
  <span class="claim claim-organic">ORGANIC</span>
  <span class="claim claim-certified">CERTIFIED</span>
  <div class="rule rule-left-2"></div>
  <div class="rule rule-right-2"></div>
  <div class="continent" role="img" aria-label="Map of the African continent in striped gold"></div>
  <span class="claim claim-ethical">ETHICALLY PRODUCED</span>
  <p class="origin">SOURCED FROM ZAMBIA’S<br>PRISTINE MIOMBO FORESTS</p>
</main>
</body>
</html>
```